Modern claims management company

We need a new company presentation brochure, composed of about 20 pages in A4 format.
Cover, page 1 who we are, page 2 company profile, page 3 territorial operation, page from 4 to 10 services offered and description of services (The title of the page are: Perizie e Liquidazione danni, riparazioni e sostituzioni, teleclaimer, accertamento danni da fenomeno elettrico, TPA, Auditing, drone pilot, Valutazione rischi), from 11 to 17 specializations (Sinistri gravi, R.C., Tecnologici, Energie rinnovabili, strutture, ambiente) page 18 e 19 integrated services (perdite occulte, ricerca guasti, indagini termografiche, crisis management), page 20 clients ( list companies and logos) page 21 contact.
The company is made up of various companies, which belong to the principal, each of which deals with specific activities.
To date we already have various logos of the main company (Vardano and Pescetti) as well as the logos of the other companies. I load them on the portal.
Found then the graphic solution that we like we will have to proceed to make a presentation in similar powerpoint and the website.

Target Market(s)

Insurance Company, Insurance Broker

Font styles to use
Other font styles liked:
• ARIAL

Colors
333333
5c5c5c
959595
0392cd

Requirements
Must have
• It must be clear, professional and modern.
Nice to have
• I indicate some competitor sites, so that you can better understand what we are doing. www.torvellsgroup.example, www.harbridgeoakes.example, www.betadomaretti.example, www.gruppotavesi.example, www.vantuzzi.example.

```html
<!DOCTYPE html>
<html lang="it">
<head>
<meta charset="utf-8">
<title>Vardano and Pescetti – Services</title>
<link href="https://fonts.googleapis.com/css2?family=Arimo:wght@400&display=swap" rel="stylesheet">
<style>
  :root {
    --frame: #3a3b3d;
    --metal-light: #d6d7d9;
    --metal-mid: #b9babd;
    --metal-dark: #8e8f92;
    --brand-blue: #0a6fbf;
    --brand-blue-deep: #0560a8;
    --text: #111111;
    --white: #ffffff;
  }
  html, body {
    margin: 0;
    padding: 0;
    overflow: hidden;
  }
  body {
    width: 847px;
    height: 1200px;
    background: var(--frame);
    font-family: "Arimo", Arial, sans-serif;
  }
  .page {
    position: relative;
    width: 847px;
    height: 1200px;
    overflow: hidden;
    background: linear-gradient(180deg, #4a4b4e 0%, #2f3032 100%);
  }
  .sheet {
    position: absolute;
    left: 20px;
    top: 20px;
    width: 807px;
    height: 1160px;
    background:
      repeating-linear-gradient(0deg, rgba(255,255,255,0.05) 0 1px, rgba(0,0,0,0.03) 1px 3px),
      linear-gradient(180deg, var(--metal-mid) 0%, var(--metal-light) 30%, var(--metal-mid) 55%, var(--metal-light) 80%, var(--metal-mid) 100%);
  }
  .brand {
    position: absolute;
    left: 40px;
    top: 44px;
    display: flex;
    align-items: center;
    gap: 10px;
    color: var(--brand-blue);
    font-size: 38px;
    line-height: 1;
    font-weight: 400;
    white-space: nowrap;
  }
  .brand-mark {
    width: 14px;
    height: 14px;
    background: var(--brand-blue);
  }
  .section-bar {
    position: absolute;
    height: 33px;
    width: 300px;
    background: linear-gradient(180deg, #1880cc 0%, var(--brand-blue-deep) 100%);
    border: 1px solid rgba(255,255,255,0.35);
    color: var(--white);
    font-size: 24px;
    line-height: 33px;
    text-align: center;
    box-sizing: border-box;
  }
  .section-bar.services { left: 20px; top: 131px; }
  .section-bar.description { left: 527px; top: 369px; }
  .copy {
    position: absolute;
    left: 42px;
    width: 770px;
    margin: 0;
    color: var(--text);
    font-size: 14.6px;
    line-height: 17.4px;
    white-space: nowrap;
  }
  .item::before {
    content: "";
    display: inline-block;
    width: 13px;
    height: 13px;
    margin: 0 12px 0 -2px;
    vertical-align: -1px;
    background: var(--brand-blue);
    border: 1px solid rgba(0,0,0,0.25);
    box-sizing: border-box;
  }
  .page-number {
    position: absolute;
    right: 40px;
    top: 1139px;
    font-size: 15px;
    color: var(--text);
  }
</style>
</head>
<body>
<div class="page">
  <div class="sheet"></div>

  <div class="brand"><span class="brand-mark"></span>Vardano and Pescetti</div>

  <h2 class="section-bar services">Services</h2>

  <p class="copy" style="top:182px">Sed ut perspiciatis unde omnis iste natus isisa error sit voluptatem accusantium doloremque architecto<br>laudantium, totam rem aperiam,eaque ipsa po quae ab illo inventore veritatis et quasi delmas architecto<br>architecto beatae vitae dicta sunt explicabo. Nemo enim ipsam voluptatem quia voluptas sit aspernatur<br>aut odit aut fugit, sed quia consequuntur magni dolores eos qui ratione voluptatem sequi nesciunt. Mita<br>Neque porro quisquam est, qui dolorem ipsum quia dolor sit amet, consectetur, adipisci velit, sed quia<br>non numquam eius modi tempora incidunt ut labore et dolore magnam aliquam quaerat voluptatem. Re<br>Ut enim ad minima veniam, quis nostrum exercitationem ullam corporis suscipit laboriosam, nisi ut eine<br>aliquid ex ea commodi consequatur? Quis autem vel eum iure reprehenderit qui in ea voluptate velit for<br>esse quam nihil molestiae consequatur, vel illum qui dolorem eum fugiat quo voluptas nulla pariatur?"</p>

  <h2 class="section-bar description">Description</h2>

  <p class="copy item" style="top:424px">At perspiciatis unde omnis iste natus isisa error sit voluptatem accusantium doloremque architecto<br>laudantium, totam rem aperiam,eaque ipsa po quae ab illo inventore veritatis et quasi delmas architecto<br>architecto beatae vitae dicta sunt explicabo. Nemo enim ipsam voluptatem quia voluptas sit aspernatur<br>aut odit aut fugit, sed quia consequuntur magni dolores eos qui ratione voluptatem sequi nesciunt. Mita</p>

  <p class="copy item" style="top:517px">At perspiciatis unde omnis iste natus isisa error sit voluptatem accusantium doloremque architecto<br>laudantium, totam rem aperiam,eaque ipsa po quae ab illo inventore veritatis et quasi delmas architecto<br>architecto beatae vitae dicta sunt explicabo. Nemo enim ipsam voluptatem quia voluptas sit aspernatur<br>aut odit aut fugit, sed quia consequuntur magni dolores eos qui ratione voluptatem sequi nesciunt. Mita<br>Neque porro quisquam est, qui dolorem ipsum quia dolor sit amet, consectetur, adipisci velit, sed quia<br>non numquam eius modi tempora incidunt ut labore et dolore magnam aliquam quaerat voluptatem. Re<br>Ut enim ad minima veniam, quis nostrum exercitationem ullam corporis suscipit laboriosam, nisi ut eine<br>aliquid ex ea commodi consequatur? Quis autem vel eum iure reprehenderit qui in ea voluptate velit for<br>esse quam nihil molestiae consequatur, vel illum qui dolorem eum fugiat quo voluptas nulla pariatur?"</p>

  <p class="copy item" style="top:702px">At perspiciatis unde omnis iste natus isisa error sit voluptatem accusantium doloremque architecto<br>laudantium, totam rem aperiam,eaque ipsa po quae ab illo inventore veritatis et quasi delmas architecto<br>architecto beatae vitae dicta sunt explicabo. Nemo enim ipsam voluptatem quia voluptas sit aspernatur<br>aut odit aut fugit, sed quia consequuntur magni dolores eos qui ratione voluptatem sequi nesciunt. Mita</p>

  <p class="copy item" style="top:796px">At perspiciatis unde omnis iste natus isisa error sit voluptatem accusantium doloremque architecto<br>laudantium, totam rem aperiam,eaque ipsa po quae ab illo inventore veritatis et quasi delmas architecto<br>architecto beatae vitae dicta sunt explicabo. Nemo enim ipsam voluptatem quia voluptas sit aspernatur<br>aut odit aut fugit, sed quia consequuntur magni dolores eos qui ratione voluptatem sequi nesciunt. Mita<br>Neque porro quisquam est, qui dolorem ipsum quia dolor sit amet, consectetur, adipisci velit, sed quia<br>non numquam eius modi tempora incidunt ut labore et dolore magnam aliquam quaerat voluptatem. Re<br>Ut enim ad minima veniam, quis nostrum exercitationem ullam corporis suscipit laboriosam, nisi ut eine<br>aliquid ex ea commodi consequatur? Quis autem vel eum iure reprehenderit qui in ea voluptate velit for<br>esse quam nihil molestiae consequatur, vel illum qui dolorem eum fugiat quo voluptas nulla pariatur?"</p>

  <div class="page-number">Page 4</div>
</div>
</body>
</html>
```